Velto Bathrooms Facelift. Moving the business in to the next professional level.

I'm currently revamping my bathroom renovation business. Part of this revamp includes our marketing strategy to better position ourselves as a professional business. As the name suggests, we primarily do bathroom renovations of all shapes, sizes and budgets. I'd like a business card design that is simple, yet displays our company as sophisticated.
What I'd like is to have a card that incorporates the following elements;
- Orange set as the primary colour and Charcoal/Grey as a complement colour. The card can also include white and/or black.
- I'd like a hexagon pattern within the charcoal/grey (In gloss perhaps to break it up a bit)
- I only want the Velto Bathrooms logo on the front of the card
- Back of the card would include contact details
- The bottom edges of the card would be rounded off
- I've attached the company name. I'd like to keep velto as it is. Bathrooms can be modified
Industry/Entity Type
Marketing

```html
<!DOCTYPE html>
<html lang="en">
<head>
<meta charset="utf-8">
<title>Velto Bathrooms – Business Card</title>
<link rel="stylesheet" href="https://fonts.googleapis.com/css2?family=Oswald:wght@300;500&display=swap">
<style>
  :root {
    --stage: #e9e6e1;
    --paper: #fbfbfb;
    --ink: #141414;
    --charcoal: #2f3133;
    --charcoal-light: #45484b;
    --orange: #f27a1a;
    --grey-light: #d9d9d9;
    --white: #ffffff;
    --text: #3a3a3a;
  }
  html, body {
    margin: 0;
    width: 1200px;
    height: 682px;
    overflow: hidden;
    background: var(--stage);
    font-family: "Oswald", "Arial Narrow", sans-serif;
  }
  .card {
    position: absolute;
    top: 187px;
    width: 540px;
    height: 308px;
    overflow: hidden;
    border-radius: 0 0 24px 24px;
    box-shadow: 0 10px 28px rgba(0,0,0,.18);
  }

  /* Front: logo only */
  .card-front {
    left: 40px;
    background: var(--charcoal);
  }
  .hex-field {
    position: absolute; inset: 0;
    background: radial-gradient(ellipse at 30% 25%, var(--charcoal-light), var(--charcoal) 70%);
  }
  .front-strip {
    position: absolute; left: 0; right: 0; bottom: 0; height: 22px;
    background: var(--orange);
  }
  .brand {
    position: absolute; left: 0; right: 0; top: 62px;
    text-align: center;
    color: var(--orange);
    font-weight: 300;
  }
  .brand-name {
    display: block;
    font-size: 112px;
    line-height: 1;
    letter-spacing: 4px;
  }
  .brand-sub {
    display: block;
    font-size: 22px;
    letter-spacing: 8px;
    margin-top: 6px;
  }

  /* Back: contact details */
  .card-back {
    left: 620px;
    background: linear-gradient(180deg, var(--white), var(--paper) 60%, #f1f1f1);
  }
  .top-strip {
    position: absolute; left: 0; right: 0; top: 0; height: 14px;
    background: var(--ink);
  }
  .name-band {
    position: absolute; left: 40px; right: 0; top: 58px; height: 36px;
    background: var(--ink);
    display: flex; align-items: center;
    color: var(--white);
  }
  .name-icon {
    width: 36px; height: 36px; flex: none;
    background: var(--orange);
    display: flex; align-items: center; justify-content: center;
  }
  .person-name {
    font-weight: 500; font-size: 20px; letter-spacing: 1px; margin-left: 14px;
  }
  .role {
    margin-left: auto; margin-right: 20px;
    font-weight: 300; font-size: 12px; letter-spacing: 2px;
  }
  .side-block {
    position: absolute; left: 40px; top: 94px; width: 36px; height: 24px;
    background: var(--grey-light);
  }
  .contacts {
    position: absolute; left: 96px; top: 116px;
    display: grid; grid-template-columns: 180px 240px; row-gap: 12px;
    font-weight: 300; font-size: 14px; color: var(--text);
  }
  .contact { display: flex; align-items: center; gap: 9px; }
  .contact svg { width: 14px; height: 14px; flex: none; }
  .address-band {
    position: absolute; left: 40px; right: 0; top: 190px; height: 30px;
    background: var(--orange);
    display: flex; align-items: center; gap: 10px; padding-left: 14px;
    color: var(--white); font-weight: 300; font-size: 13px; letter-spacing: .5px;
  }
  .address-band svg { width: 12px; height: 15px; flex: none; }
  .bottom-band {
    position: absolute; left: 0; right: 0; bottom: 0; height: 44px;
    background: linear-gradient(90deg, var(--charcoal), var(--charcoal-light));
  }
</style>
</head>
<body>
  <div class="card card-front">
    <div class="hex-field" role="img" aria-label="Glossy charcoal hexagon pattern"></div>
    <div class="brand">
      <span class="brand-name">velto</span>
      <span class="brand-sub">BATHROOMS</span>
    </div>
    <div class="front-strip"></div>
  </div>

  <div class="card card-back">
    <div class="top-strip"></div>

    <div class="name-band">
      <div class="name-icon">
        <svg width="20" height="20" viewBox="0 0 26 26" aria-hidden="true">
          <circle cx="13" cy="8" r="5.5" fill="#ffffff"/>
          <path d="M2 25 Q2 15 13 15 Q24 15 24 25 Z" fill="#ffffff"/>
        </svg>
      </div>
      <span class="person-name">DANIEL REEVE</span>
      <span class="role">GENERAL MANAGER</span>
    </div>
    <div class="side-block"></div>

    <div class="contacts">
      <div class="contact">
        <svg viewBox="0 0 18 18" aria-hidden="true"><path d="M4 1h3l1.5 4-2 1.5a10 10 0 0 0 5 5L13 9.5l4 1.5v3c0 1.5-1 2.5-2.5 2.5C7 16.5 1.5 11 1.5 3.5 1.5 2 2.5 1 4 1z" fill="#f27a1a"/></svg>
        014 552 8810
      </div>
      <div class="contact">
        <svg viewBox="0 0 18 18" aria-hidden="true"><rect x="1" y="4" width="16" height="11" fill="#f27a1a"/><path d="M1 4l8 6 8-6" fill="none" stroke="#fbfbfb" stroke-width="1.4"/></svg>
        hello@veltobath.com
      </div>
      <div class="contact">
        <svg viewBox="0 0 18 18" aria-hidden="true"><rect x="3" y="1.5" width="12" height="15" rx="1.5" fill="none" stroke="#f27a1a" stroke-width="2"/></svg>
        014 552 8811
      </div>
      <div class="contact">
        <svg viewBox="0 0 18 18" aria-hidden="true"><circle cx="9" cy="9" r="7.5" fill="none" stroke="#f27a1a" stroke-width="1.6"/><ellipse cx="9" cy="9" rx="3.2" ry="7.5" fill="none" stroke="#f27a1a" stroke-width="1.3"/><path d="M1.5 9h15" stroke="#f27a1a" stroke-width="1.3"/></svg>
        www.veltobathrooms.com
      </div>
    </div>

    <div class="address-band">
      <svg viewBox="0 0 16 20" aria-hidden="true"><path d="M8 0a7 7 0 0 0-7 7c0 5 7 13 7 13s7-8 7-13a7 7 0 0 0-7-7z" fill="#ffffff"/><circle cx="8" cy="7" r="2.6" fill="#f27a1a"/></svg>
      42 Harbor Lane, Unit 3, Crestview Road
    </div>
    <div class="bottom-band" role="img" aria-label="Glossy charcoal hexagon pattern"></div>
  </div>
</body>
</html>
```